Lumen Ridge Agency Stationery
Lumen Ridge
Project: Lumen Ridge Agency Stationery
Lumen Ridge Agency Stationery - Advertising
Creative Brief
Simple
Doris Jean Malloway
Vice President, Corporate Operations
482 Fenwick Ave. Seattle, WA 98112
info@lumenridgeco.example
dorisjean@lumenridgeco.example
www.lumenridgeco.example
Front should have black background with LR circle only (no text). Would love to see the red circle and red plus raised to give them a 3-D look. You can do a standard rectangle business card or change it up and make it a circle.
Back should also be black background with white font. Occasionally you can use a red font if it looks cool to distinguish individual fields. Around the border of the card should be the company information (Address field, phone number (toll-free field), email (fax field), and website. Inside the center should be the person's name, title, direct line (phone field) and email. You can put the logo in the center again if it looks like to have that on the left and contact info on right, but it is not necessary to use the logo again. You can also try using icons with the text fields, but if it looks too busy, then don't worry about it. Thanks!

```html
<!DOCTYPE html>
<html lang="en">
<head>
<meta charset="utf-8">
<title>Lumen Ridge Agency Stationery</title>
<link rel="stylesheet" href="https://fonts.googleapis.com/css2?family=Montserrat:wght@400;600&family=Open+Sans:wght@400;600&display=swap">
<style>
  :root {
    --stage: #e7e7e7;
    --ink: #0d0d0d;
    --red: #e3161b;
    --white: #ffffff;
    --grey-text: #6a6a6a;
  }
  * { margin: 0; padding: 0; box-sizing: border-box; }
  html, body { width: 1200px; height: 838px; overflow: hidden; }
  body {
    background: var(--stage);
    position: relative;
    font-family: "Open Sans", Arial, sans-serif;
  }

  /* Black side: name and web address */
  .card-back {
    position: absolute;
    left: 600px; top: 120px;
    width: 520px; height: 297px;
    background: var(--ink);
    display: flex; flex-direction: column;
    align-items: center; justify-content: center;
    gap: 22px;
  }
  .back-name {
    font-family: "Montserrat", Arial, sans-serif;
    font-weight: 400;
    font-size: 44px;
    color: var(--white);
    letter-spacing: 1px;
  }
  .back-web {
    font-family: "Montserrat", Arial, sans-serif;
    font-size: 15px;
    color: var(--white);
    letter-spacing: 1.5px;
  }
  .back-web .accent { color: var(--red); }

  /* Red and white side */
  .card-front {
    position: absolute;
    left: 80px; top: 400px;
    width: 540px; height: 309px;
    background: var(--ink);
    padding: 10px;
  }
  .front-inner {
    position: relative;
    width: 100%; height: 100%;
    background: var(--white);
    overflow: hidden;
  }
  .front-sweep { position: absolute; left: 0; top: 0; }
  .front-brand {
    position: absolute; left: 34px; top: 34px;
    display: flex; align-items: center; gap: 14px;
  }
  .brand-circle {
    width: 62px; height: 62px; border-radius: 50%;
    background: var(--white);
    border: 3px solid var(--ink);
  }
  .brand-name {
    font-family: "Montserrat", Arial, sans-serif;
    font-size: 30px; font-weight: 400;
    color: var(--white);
  }
  .person {
    position: absolute; left: 245px; top: 100px;
    color: var(--white);
  }
  .person-name { font-size: 14px; font-weight: 600; }
  .person-title { font-size: 8px; margin-top: 2px; }

  .contacts {
    position: absolute; left: 24px; right: 20px; top: 190px;
    display: grid; grid-template-columns: 1.35fr 1fr;
    row-gap: 9px; column-gap: 14px;
  }
  .contact {
    display: flex; align-items: center; gap: 7px;
    font-size: 9.5px; color: var(--grey-text);
    white-space: nowrap;
  }
  .contact svg { flex: none; }
</style>
</head>
<body>

  <section class="card-back">
    <p class="back-name">Lumen Ridge</p>
    <p class="back-web"><span class="accent">www.</span>lumenridgeco<span class="accent">.example</span></p>
  </section>

  <section class="card-front">
    <div class="front-inner">
      <svg class="front-sweep" width="520" height="289" viewBox="0 0 520 289">
        <path d="M0 0 H520 V110 C400 170 200 185 0 165 Z" fill="var(--red)"/>
        <path d="M0 165 C200 185 400 170 520 110" fill="none" stroke="var(--ink)" stroke-width="4"/>
      </svg>

      <div class="front-brand">
        <span class="brand-circle"></span>
        <span class="brand-name">Lumen Ridge</span>
      </div>

      <div class="person">
        <p class="person-name">Doris Jean Malloway</p>
        <p class="person-title">Vice President, Corporate Operations</p>
      </div>

      <div class="contacts">
        <p class="contact">
          <svg width="14" height="14" viewBox="0 0 14 14"><circle cx="7" cy="7" r="7" fill="var(--red)"/><path d="M7 3 a2.4 2.4 0 0 1 2.4 2.4 C9.4 7.4 7 10.5 7 10.5 S4.6 7.4 4.6 5.4 A2.4 2.4 0 0 1 7 3z" fill="#fff"/></svg>
          482 Fenwick Ave. Seattle, WA 98112
        </p>
        <p class="contact">
          <svg width="14" height="14" viewBox="0 0 14 14"><circle cx="7" cy="7" r="7" fill="var(--red)"/><path d="M4.5 3.5 L6 3.5 L6.6 5.5 L5.6 6.3 C6.1 7.4 6.9 8.2 7.9 8.7 L8.7 7.7 L10.6 8.3 L10.6 9.8 C7.2 10.2 4 7 4.5 3.5Z" fill="#fff"/></svg>
          206.555.0147
        </p>
        <p class="contact">
          <svg width="14" height="14" viewBox="0 0 14 14"><circle cx="7" cy="7" r="7" fill="var(--red)"/><rect x="3.5" y="4.5" width="7" height="5" fill="#fff"/><path d="M3.5 4.5 L7 7.5 L10.5 4.5" stroke="var(--red)" stroke-width="0.8" fill="none"/></svg>
          info@lumenridgeco.example
        </p>
        <p class="contact">
          <svg width="14" height="14" viewBox="0 0 14 14"><circle cx="7" cy="7" r="7" fill="var(--red)"/><path d="M4.5 3.5 L6 3.5 L6.6 5.5 L5.6 6.3 C6.1 7.4 6.9 8.2 7.9 8.7 L8.7 7.7 L10.6 8.3 L10.6 9.8 C7.2 10.2 4 7 4.5 3.5Z" fill="#fff"/></svg>
          206.555.0192
        </p>
        <p class="contact">
          <svg width="14" height="14" viewBox="0 0 14 14"><circle cx="7" cy="7" r="7" fill="var(--red)"/><rect x="3.5" y="4.5" width="7" height="5" fill="#fff"/><path d="M3.5 4.5 L7 7.5 L10.5 4.5" stroke="var(--red)" stroke-width="0.8" fill="none"/></svg>
          dorisjean@lumenridgeco.example
        </p>
        <p class="contact">
          <svg width="14" height="14" viewBox="0 0 14 14"><circle cx="7" cy="7" r="7" fill="var(--red)"/><circle cx="7" cy="7" r="3.6" fill="none" stroke="#fff" stroke-width="1"/><path d="M3.4 7 H10.6 M7 3.4 C5.5 5.5 5.5 8.5 7 10.6 M7 3.4 C8.5 5.5 8.5 8.5 7 10.6" stroke="#fff" stroke-width="0.8" fill="none"/></svg>
          www.lumenridgeco.example
        </p>
      </div>
    </div>
  </section>

</body>
</html>
```